Satchel & Compass needs new business card design

I need a new business card design. I'm looking for out-of-the-box design which represents the freedom of being a location independent entrepreneur.
I offer coaching, retreats and trips.
I would like to see designs with and without the photo.
Colors I use are black (#000000), green (#25A796) and brown (#D7C38C)
Website satchelandcompass.com

Target Market(s)

location independent entrepreneurs, digital nomads, people looking to swap the 9 to 5 for a lifestyle business

Industry/Entity Type

Business

Contact Information for Business Card

Petra Varga
Your Lifestyle Business Coach, Retreat & Trip Leader
http://satchelandcompass.com
hello@satchelandcompass.com
Live a life you don't need a holiday from

Font styles to use
Serif
Sans Serif

Requirements
Must have
• One side should contain only the logo. I would also consider having the "Live a life you don't need a holiday from" on that side too (depending on how it looks)
• Please show both sides on the designs.

```html
<!DOCTYPE html>
<html lang="en">
<head>
<meta charset="utf-8">
<title>Petra Varga – Business Card</title>
<link href="https://fonts.googleapis.com/css2?family=Questrial&family=Open+Sans:wght@400;600&display=swap" rel="stylesheet">
<style>
  :root {
    --page-bg: #1c1c1c;
    --card-black: #0e0e0e;
    --card-charcoal: #2b2b2b;
    --band-mid: #6f6f6f;
    --band-light: #b9b9b9;
    --paper: #f4f4f4;
    --paper-shade: #dcdcdc;
    --ink-white: #f2f2f2;
    --ink-soft: #c9c9c9;
    --ink-dark: #3a3a3a;
  }
  * { box-sizing: border-box; margin: 0; padding: 0; }
  html, body { width: 1200px; height: 900px; overflow: hidden; }
  body {
    background: var(--page-bg);
    font-family: "Open Sans", sans-serif;
    display: flex;
    flex-direction: column;
    align-items: center;
    justify-content: center;
    gap: 40px;
  }
  .card {
    width: 700px;
    height: 400px;
    position: relative;
    overflow: hidden;
    box-shadow: 0 14px 30px rgba(0,0,0,.55);
  }
  /* Front */
  .card-front {
    background:
      repeating-linear-gradient(0deg, rgba(255,255,255,.018) 0 1px, transparent 1px 3px),
      linear-gradient(160deg, var(--card-charcoal) 0%, var(--card-black) 75%);
    display: flex;
    flex-direction: column;
    align-items: center;
    justify-content: center;
  }
  .identity { text-align: right; }
  .name {
    font-family: "Questrial", sans-serif;
    color: var(--ink-white);
    font-weight: 400;
    letter-spacing: 1px;
    line-height: 1;
  }
  .card-front .name { font-size: 72px; }
  .role {
    font-family: "Open Sans", sans-serif;
    font-weight: 600;
    color: var(--ink-soft);
    margin-top: 4px;
  }
  .card-front .role { font-size: 15px; }

  /* Back */
  .card-back { display: flex; background: var(--card-black); }
  .logo-panel {
    width: 52%;
    background: linear-gradient(170deg, var(--paper) 0%, var(--paper-shade) 100%);
    display: flex;
    align-items: flex-start;
    padding: 80px 0 0 40px;
  }
  .logo-name {
    font-family: "Open Sans", sans-serif;
    font-weight: 600;
    font-size: 30px;
    color: var(--ink-dark);
    letter-spacing: .5px;
  }
  .band-light { width: 7%; background: var(--band-light); }
  .band-mid { width: 6%; background: var(--band-mid); }
  .details-panel {
    flex: 1;
    background: linear-gradient(165deg, var(--card-charcoal) 0%, var(--card-black) 80%);
    display: flex;
    flex-direction: column;
    justify-content: space-between;
    padding: 44px 24px 34px 20px;
  }
  .card-back .name { font-size: 34px; }
  .card-back .role { font-size: 8px; margin-top: 2px; }
  .contacts { list-style: none; display: flex; flex-direction: column; gap: 10px; }
  .contacts li {
    display: flex;
    align-items: center;
    gap: 10px;
    font-size: 13px;
    color: var(--ink-white);
  }
  .contacts svg { width: 14px; height: 14px; flex: none; }
</style>
</head>
<body>
  <section class="card card-front" aria-label="Card front">
    <div class="identity">
      <h1 class="name">Petra Varga</h1>
      <p class="role">Your Lifestyle Business Coach, Retreat &amp; Trip Leader</p>
    </div>
  </section>

  <section class="card card-back" aria-label="Card back">
    <div class="logo-panel">
      <span class="logo-name">Satchel &amp; Compass</span>
    </div>
    <div class="band-light"></div>
    <div class="band-mid"></div>
    <div class="details-panel">
      <div class="identity">
        <h2 class="name">Petra Varga</h2>
        <p class="role">Your Lifestyle Business Coach, Retreat &amp; Trip Leader</p>
      </div>
      <ul class="contacts">
        <li>
          <svg viewBox="0 0 16 16" aria-hidden="true"><circle cx="8" cy="8" r="7" fill="none" stroke="#f2f2f2" stroke-width="1.4"/><path d="M1 8h14M8 1c-3 3-3 11 0 14M8 1c3 3 3 11 0 14" fill="none" stroke="#f2f2f2" stroke-width="1.2"/></svg>
          http://satchelandcompass.com
        </li>
        <li>
          <svg viewBox="0 0 16 16" aria-hidden="true"><rect x="1" y="3" width="14" height="10" fill="#f2f2f2"/><path d="M1 3l7 6 7-6" fill="none" stroke="#2b2b2b" stroke-width="1.2"/></svg>
          hello@satchelandcompass.com
        </li>
      </ul>
    </div>
  </section>
</body>
</html>
```